Dozevale 250 ml pouch design (190 x 120 mm) + logo.

Dozevale is a startup that focuses on one product: a powder supplement that intends to improve sleep quality (as opposed to melatonin products that focus on falling asleep). The target demographic is basically anyone with poor sleep but mostly adults (aged 30 - 45) who experience that bad sleep affects daily work performance.

The formula is a combination of glycine (3 g), magnesium bisglycinate (200 mg elemental), ashwagandha extract QRT-41 (300 mg), lemon balm extract (200 mg) and L-theanine (200 mg), and supporting ingredients inulin and natural cherry flavoring. Net weight will be approximately 180 - 190 grams with 30 servings.

For this product I seek a design for the pouch it comes in and the logo that accompanies it. For pouch reference, it is the 250 ml "Sturdy Sparrow" stand-up pouch from Wrapnelo.

Regarding pouch design, I'm thinking of the color blue with perhaps nuances of red or purple. Style should be relatively minimalist and convey trust. I would like to see some sort of ingredient stack on the front of the pouch to increase transparency and trust. The back of the pouch should leave room for the barcode, company details, regulatory claims (warnings), ingredient listing (again), allergy information, usage recommendation. These should be treated as text boxes that I can edit later.

The logo should of course mimic this style. One concrete idea that came to mind is to make some sort of stack icon (e.g. bars stacking) somewhere, perhaps in a letter S. This should represent the building of better quality sleep/ improving your sleep performance. Another angle could be the ingredient stack that helps achieve this. The stack icon could become the favicon/ textless logo.

The website is still in the making but will incorporate design elements of websites from Zorbly, Pebble vitals, Tiers vitals, Nine doze.

Font styles to use
Sans Serif

Colors
0054AA
0677BA
7BADD7
CADEEF
E8F1F8

```html
<!DOCTYPE html>
<html lang="en">
<head>
<meta charset="utf-8">
<title>Dozevale Pouch Front</title>
<link rel="stylesheet" href="https://fonts.googleapis.com/css2?family=Poppins:wght@400;500;600&display=swap">
<style>
  :root {
    --backdrop: #d2eaf1;
    --navy: #0a1f6b;
    --brand-blue: #0054aa;
    --mid-blue: #0677ba;
    --soft-blue: #7badd7;
    --pale-blue: #cadeef;
    --mist: #e8f1f8;
    --white: #ffffff;
  }
  html, body {
    margin: 0;
    padding: 0;
    width: 1200px;
    height: 960px;
    overflow: hidden;
    background: var(--backdrop);
    font-family: "Poppins", sans-serif;
  }
  .canvas {
    position: relative;
    width: 1200px;
    height: 960px;
  }
  .pouch-front {
    position: absolute;
    left: 350px;
    top: 96px;
    width: 500px;
    height: 768px;
  }
  .pouch-art {
    position: absolute;
    inset: 0;
    display: block;
  }
  .brand-lockup {
    position: absolute;
    left: 0;
    right: 0;
    top: 268px;
    display: flex;
    flex-direction: column;
    align-items: center;
  }
  .brand-dot {
    width: 140px;
    height: 140px;
    border-radius: 50%;
    background: var(--mid-blue);
  }
  .brand-name {
    margin-top: 18px;
    font-weight: 600;
    font-size: 50px;
    line-height: 1;
    letter-spacing: -0.5px;
    color: var(--navy);
  }
  .product-type {
    position: absolute;
    left: 0;
    right: 0;
    top: 642px;
    text-align: center;
    font-weight: 600;
    font-size: 14px;
    letter-spacing: 4px;
    color: var(--brand-blue);
  }
  .net-content {
    position: absolute;
    left: 116px;
    top: 672px;
    width: 268px;
    height: 28px;
    border-radius: 14px;
    background: linear-gradient(90deg, var(--navy), var(--brand-blue) 60%, var(--soft-blue));
    color: var(--white);
    font-weight: 400;
    font-size: 13px;
    letter-spacing: 1.6px;
    display: flex;
    align-items: center;
    justify-content: center;
  }
</style>
</head>
<body>
<main class="canvas">
  <section class="pouch-front">
    <svg class="pouch-art" width="500" height="768" viewBox="0 0 500 768" aria-hidden="true">
      <defs>
        <clipPath id="pouch-shape">
          <rect x="0" y="0" width="500" height="768" rx="22" ry="22"/>
        </clipPath>
        <linearGradient id="pouch-base" x1="0" y1="0" x2="0" y2="1">
          <stop offset="0" stop-color="#f6f7f8"/>
          <stop offset="1" stop-color="#e8f1f8"/>
        </linearGradient>
        <linearGradient id="lower-blue" x1="0" y1="0" x2="1" y2="0">
          <stop offset="0" stop-color="#5f93b8"/>
          <stop offset="0.7" stop-color="#a8cdea"/>
          <stop offset="1" stop-color="#8dbbe0"/>
        </linearGradient>
      </defs>
      <g clip-path="url(#pouch-shape)">
        <rect class="pouch-base" width="500" height="768" fill="url(#pouch-base)"/>
        <!-- zipper seal -->
        <rect x="0" y="100" width="500" height="14" fill="#eceeef"/>
        <!-- outer band -->
        <path d="M0 209 Q250 80 500 209 L500 551 Q250 660 0 551 Z" fill="#cadeef" opacity="0.75"/>
        <!-- inner band -->
        <path d="M0 312 Q250 190 500 312 L500 449 Q250 555 0 449 Z" fill="#7badd7" opacity="0.45"/>
        <!-- lower blue field -->
        <path d="M0 551 Q250 660 0 551 Z M0 551 Q250 660 500 551 L500 768 L0 768 Z" fill="url(#lower-blue)"/>
      </g>
      <!-- hang hole -->
      <path d="M196 48 H236 A14 12 0 0 1 264 48 H304 A8 8 0 0 1 304 70 H196 A8 8 0 0 1 196 48 Z" fill="#d2eaf1"/>
    </svg>

    <div class="brand-lockup">
      <div class="brand-dot"></div>
      <div class="brand-name">dozevale</div>
    </div>

    <p class="product-type" style="margin:0">SLEEP ENHANCING POWDER</p>
    <div class="net-content">180 GM | 30 SERVINGS</div>
  </section>
</main>
</body>
</html>
```